Dune Air & Plus business card

I need an awesome, double-sided business card designed with our new logo. I would like the one side black with the colored logo, and the back side is all yours. I'd like to see horizontal and vertical layouts. Get creative! Thank you.

Target Market(s)

HVAC, Heating and Cooling in Phoenix, AZ

Industry/Entity Type

HVAC

Contact Information for Business Card

We need our new logo on the card. Tom Harker, (623) 555-0142, tom@trydunesair.com, www.trydunesair.com, ROC 514273

```html
<!DOCTYPE html>
<html lang="en">
<head>
<meta charset="utf-8">
<title>Dune Air &amp; Plus – Business Card</title>
<link href="https://fonts.googleapis.com/css2?family=Montserrat:wght@400;500;600;800&display=swap" rel="stylesheet">
<style>
  :root {
    --page-bg: #ebeceb;
    --card-dark: #2a2928;
    --accent-orange: #f08321;
    --text-light: #ffffff;
  }
  html, body {
    margin: 0;
    padding: 0;
    width: 1200px;
    height: 1067px;
    overflow: hidden;
    background: var(--page-bg);
    font-family: "Montserrat", sans-serif;
  }
  .card {
    position: absolute;
    left: 351px;
    width: 497px;
    height: 266px;
    border-radius: 15px;
    overflow: hidden;
    background: var(--card-dark);
  }
  .card--front { top: 220px; }
  .card--back { top: 612px; }
  .card__shapes {
    position: absolute;
    inset: 0;
    width: 497px;
    height: 266px;
  }
  .shape-orange { fill: var(--accent-orange); }
  .shape-dark { fill: var(--card-dark); }

  .brand-name {
    position: absolute;
    margin: 0;
    color: var(--text-light);
    font-family: "Montserrat", sans-serif;
    font-weight: 800;
    white-space: nowrap;
    letter-spacing: 0.5px;
  }
  .brand-name--band {
    left: 44px;
    top: 120px;
    font-size: 17px;
    line-height: 24px;
  }
  .brand-name--circle {
    width: 170px;
    text-align: center;
    font-size: 17px;
    line-height: 24px;
  }
  .card--front .brand-name--circle { left: 261px; top: 121px; }
  .card--back .brand-name--circle { left: 281px; top: 136px; }

  .holder-name {
    position: absolute;
    left: 26px;
    top: 22px;
    margin: 0;
    color: var(--text-light);
    font-size: 22px;
    font-weight: 400;
    letter-spacing: 0.3px;
  }
  .holder-name strong { font-weight: 600; }

  .contact-list {
    position: absolute;
    left: 24px;
    top: 118px;
    margin: 0;
    padding: 0;
    list-style: none;
  }
  .contact-list::before {
    content: "";
    position: absolute;
    left: 22px;
    top: 1px;
    width: 1px;
    height: 101px;
    background: var(--text-light);
  }
  .contact-item {
    position: relative;
    height: 27px;
    display: flex;
    align-items: center;
    color: var(--text-light);
    font-size: 13px;
    font-weight: 400;
    letter-spacing: 0.3px;
  }
  .contact-icon {
    width: 12px;
    height: 12px;
    margin-right: 18px;
    fill: none;
    stroke: var(--text-light);
    stroke-width: 1.3;
  }
</style>
</head>
<body>

<section class="card card--front" aria-label="Card front">
  <svg class="card__shapes" viewBox="0 0 497 266" aria-hidden="true">
    <rect class="shape-orange" x="0" y="108.6" width="497" height="48.4"/>
    <path class="shape-orange" d="M205 108.6 Q226 108.6 234 90 L250 112 Z"/>
    <path class="shape-orange" d="M205 157 Q226 157 234 175.6 L250 153 Z"/>
    <path class="shape-orange" d="M487 108.6 Q466 108.6 458 90 L442 112 Z"/>
    <path class="shape-orange" d="M487 157 Q466 157 458 175.6 L442 153 Z"/>
    <circle class="shape-orange" cx="346" cy="133" r="117"/>
    <circle class="shape-dark" cx="346" cy="133" r="90"/>
  </svg>
  <p class="brand-name brand-name--band">Dune Air &amp; Plus</p>
  <p class="brand-name brand-name--circle">Dune Air &amp; Plus</p>
</section>

<section class="card card--back" aria-label="Card back">
  <svg class="card__shapes" viewBox="0 0 497 266" aria-hidden="true">
    <rect class="shape-orange" x="0" y="228" width="497" height="38"/>
    <path class="shape-orange" d="M225 228 Q262 228 261 205 L300 210 L300 228 Z"/>
    <path class="shape-orange" d="M490 228 Q462 228 468 205 L430 210 L430 228 Z"/>
    <circle class="shape-orange" cx="366" cy="148" r="115"/>
    <circle class="shape-dark" cx="366" cy="148" r="95"/>
  </svg>

  <h1 class="holder-name"><strong>Tom</strong> Harker</h1>

  <ul class="contact-list">
    <li class="contact-item">
      <svg class="contact-icon" viewBox="0 0 12 12" aria-hidden="true"><path d="M3 1 L4.5 3.5 L3.5 4.8 Q4.5 7.3 7 8.5 L8.3 7.4 L11 9 L10 11 Q4 11 1 3 Z"/></svg>
      (623) 555-0142
    </li>
    <li class="contact-item">
      <svg class="contact-icon" viewBox="0 0 12 12" aria-hidden="true"><rect x="1" y="2.5" width="10" height="7"/><path d="M1 2.5 L6 6.5 L11 2.5"/></svg>
      tom@trydunesair.com
    </li>
    <li class="contact-item">
      <svg class="contact-icon" viewBox="0 0 12 12" aria-hidden="true"><circle cx="6" cy="6" r="5"/><ellipse cx="6" cy="6" rx="2.2" ry="5"/><path d="M1 6 H11 M2 3.5 H10 M2 8.5 H10"/></svg>
      www.trydunesair.com
    </li>
    <li class="contact-item">
      <svg class="contact-icon" viewBox="0 0 12 12" aria-hidden="true"><path d="M6 9 Q2.5 5.5 2.5 4 A3.5 3.5 0 0 1 9.5 4 Q9.5 5.5 6 9 Z"/><circle cx="6" cy="4" r="1.2"/><path d="M1 11 H11"/></svg>
      ROC 514273
    </li>
  </ul>

  <p class="brand-name brand-name--circle">Dune Air &amp; Plus</p>
</section>

</body>
</html>
```